vELRA AirCargo Trailer Wrap

Project: Full exterior livery design for our air cargo road transport trailer., Trailer type: Brevik Ultra Trailer
Base color: White (must remain dominant) About Us VELRA specializes in air freight road transportation. We transport air cargo:
Airport β†’ Logistics hubs
Manufacturers β†’ Airport
We are a last-mile logistics partner in the air cargo industry. A clean, modern, and highly recognizable trailer design that instantly communicates: ✈ Air Cargo πŸš› Road Transport 🌍 International Logistics πŸ”· VELRA brand The design must be minimal but strong.
Professional, premium, and visible from distance.

Design Goals
Clear and bold VELRA logo placement
Strong highway visibility
Aviation-inspired visual elements (subtle, not clichΓ©)
Modern, industrial typography
Clean composition – no clutter
Avoid: overly busy graphics, cartoon airplanes, generic stock icons.
Deliverables
Left side view
Right side view
Rear view

We are looking for a design that makes people immediately think:
β€œAir cargo. Professional. Reliable.”

Target Market(s)

Forwarding

Industry/Entity Type

Transportation

Requirements
Must have
• "LINEHAUL" tag "VELRA logo+ LINEHAUL"
Nice to have
Should not have
• Air cargo/Air freight/Express is boring..

```html
<!DOCTYPE html>
<html lang="en">
<head>
<meta charset="utf-8">
<title>VELRA Linehaul Trailer Livery</title>
<link rel="stylesheet" href="https://fonts.googleapis.com/css2?family=Montserrat:wght@500;800&family=Oswald:wght@500;700&display=swap">
<style>
  :root{
    --brand-red:#ee3e55;
    --ink:#231f20;
    --panel:#ffffff;
    --backdrop:#e9ebee;
  }
  *{margin:0;padding:0;box-sizing:border-box}
  html,body{width:1200px;height:860px;overflow:hidden;background:var(--backdrop)}
  .canvas{position:relative;width:1200px;height:860px}

  .panel{position:absolute;background:var(--panel);box-shadow:0 2px 10px rgba(0,0,0,.12);overflow:hidden}
  .side-panel{left:20px;top:230px;width:790px;height:400px}
  .rear-panel{left:840px;top:120px;width:340px;height:620px}

  .stripe{position:absolute;background:var(--brand-red)}
  .band{position:absolute;background:var(--brand-red);color:var(--panel);display:flex;align-items:center;white-space:nowrap}

  .wordmark{position:absolute;display:flex;align-items:center;gap:12px;white-space:nowrap;
    font-family:"Montserrat",sans-serif;font-weight:800;color:var(--ink);letter-spacing:-2px;line-height:1}
  .wordmark .dot{width:.28em;height:.28em;border-radius:50%;background:var(--brand-red)}

  /* side */
  .side-tag{left:0;top:170px;width:146px;height:46px;justify-content:center;
    font-family:"Oswald",sans-serif;font-weight:700;font-size:22px;letter-spacing:.5px}
  .side-panel .wordmark{left:160px;top:152px;font-size:80px}
  .side-band{left:520px;top:152px;width:270px;height:80px;padding-left:16px;
    font-family:"Montserrat",sans-serif;font-weight:800;font-size:33px;letter-spacing:.5px}
  .side-phone{position:absolute;left:14px;top:300px;display:flex;align-items:center;gap:5px;white-space:nowrap;
    font-family:"Oswald",sans-serif;font-weight:500;font-size:16px;color:var(--ink)}
  .side-web{position:absolute;left:520px;top:322px;display:flex;align-items:center;gap:8px;white-space:nowrap;
    font-family:"Montserrat",sans-serif;font-weight:500;font-size:26px;color:var(--ink)}

  /* rear */
  .rear-panel .wordmark{left:0;top:110px;width:340px;justify-content:center;font-size:66px}
  .rear-band{left:0;top:270px;width:340px;height:100px;justify-content:center;
    font-family:"Oswald",sans-serif;font-weight:700;font-size:60px;letter-spacing:.5px}
  .rear-contact{position:absolute;left:28px;top:440px;display:flex;flex-direction:column;gap:22px;
    font-family:"Oswald",sans-serif;color:var(--ink);white-space:nowrap}
  .rear-contact .line{display:flex;align-items:center;gap:10px}
  .rear-phone{font-weight:700;font-size:36px}
  .rear-web{font-weight:500;font-size:30px}

  .icon{flex:none}
</style>
</head>
<body>
<main class="canvas">

  <section class="panel side-panel" aria-label="Trailer side view">
    <div class="stripe" style="left:0;top:160px;width:146px;height:5px"></div>
    <div class="band side-tag">LINEHAUL #</div>
    <div class="stripe" style="left:0;top:221px;width:146px;height:5px"></div>

    <div class="wordmark"><span class="dot"></span>VELRA</div>

    <div class="stripe" style="left:520px;top:132px;width:270px;height:12px"></div>
    <div class="band side-band">+ LINEHAUL</div>
    <div class="stripe" style="left:520px;top:240px;width:270px;height:12px"></div>

    <div class="side-phone">
      <svg class="icon" width="14" height="16" viewBox="0 0 24 24"><path d="M6.6 2.5 9.8 6.4 8 8.8c1.1 2.6 3.4 5 6.2 6.4l2.3-1.8 3.9 3.2-1.8 3.6C11.3 20 4.4 13 3.8 4.3z" fill="var(--brand-red)"/></svg>
      +36 70 555 0142
    </div>
    <div class="side-web">
      <svg class="icon" width="30" height="30" viewBox="0 0 24 24" fill="none" stroke="var(--brand-red)" stroke-width="1.6"><circle cx="12" cy="12" r="10"/><ellipse cx="12" cy="12" rx="4.5" ry="10"/><path d="M2 12h20M4 7h16M4 17h16M12 2v20"/></svg>
      velrafreight.com
    </div>
  </section>

  <section class="panel rear-panel" aria-label="Trailer rear view">
    <div class="wordmark"><span class="dot"></span>VELRA</div>

    <div class="stripe" style="left:0;top:248px;width:340px;height:10px"></div>
    <div class="band rear-band">LINEHAUL #</div>
    <div class="stripe" style="left:0;top:382px;width:340px;height:10px"></div>

    <div class="rear-contact">
      <div class="line rear-phone">
        <svg class="icon" width="30" height="36" viewBox="0 0 24 24"><path d="M6.6 2.5 9.8 6.4 8 8.8c1.1 2.6 3.4 5 6.2 6.4l2.3-1.8 3.9 3.2-1.8 3.6C11.3 20 4.4 13 3.8 4.3z" fill="var(--brand-red)"/></svg>
        +36 70 555 0142
      </div>
      <div class="line rear-web">
        <svg class="icon" width="30" height="30" viewBox="0 0 24 24" fill="none" stroke="var(--brand-red)" stroke-width="1.6"><circle cx="12" cy="12" r="10"/><ellipse cx="12" cy="12" rx="4.5" ry="10"/><path d="M2 12h20M4 7h16M4 17h16M12 2v20"/></svg>
        velrafreight.com
      </div>
    </div>
  </section>

</main>
</body>
</html>
```